Leadership training for women Business + Spirit

I need a flyer for a leadership training to hand out after I've been doing public speaking. I would also like to send it as a PDF. so maybe A4 is a good size. I will probably also need a brochure, with some more in depth information, but to start with I like to just give them something so they get inspired to contact me for more information. You can see more of my style on www.brightlantern.se . Its a training that combines business with spirit, heart with intellect. We focus both on strict leadership skills such as Setting objectives aligned with strategy, assess performance and spiritual practices such as meditation, connecting with your unique essence. I like the deign to communicate business and professional together with warmth, life and joy. Colourful with style. Empowerment. The attached style guide does not have to be followed strictly but please use it in combination with my site www.brightlantern.se I've the logo in many different sizes. I've added the smallest one below. Use any images that you think might fit, doesn't have to be from my website, it could be from your resources. I've added some other images here in the brief too, I have many more but can't attach all of it :-).
Women in leadership positions age 30 - 60
Leadership

```html
<!DOCTYPE html>
<html lang="en">
<head>
<meta charset="utf-8">
<title>Bright Lantern – Leadership for Women</title>
<link href="https://fonts.googleapis.com/css2?family=Lato:wght@400;700;900&display=swap" rel="stylesheet">
<style>
  :root {
    --navy: #15314f;
    --white: #ffffff;
    --swoosh: #b9bcc1;
    --shadow: rgba(0,0,0,0.35);
  }
  * { box-sizing: border-box; margin: 0; padding: 0; }
  html, body { width: 950px; height: 1200px; overflow: hidden; background: var(--white); }
  body { font-family: 'Lato', Arial, sans-serif; color: var(--white); }
  .flyer { position: relative; width: 950px; height: 1200px; overflow: hidden; background: var(--white); }

  .hero-band { position: absolute; left: 0; top: 0; width: 950px; height: 400px; }
  .portrait {
    position: absolute; left: 60px; top: 50px; width: 222px; height: 262px;
    border: 3px solid var(--white); border-radius: 22px;
    background: linear-gradient(160deg, #8a6b5c 0%, #5a4a44 45%, #2a2e3a 100%);
  }
  .intro { position: absolute; left: 316px; top: 50px; width: 570px; text-align: center; }
  .intro-name { font-weight: 900; font-size: 28px; line-height: 1.2; margin-bottom: 10px; }
  .intro-text { font-size: 14.6px; line-height: 18.3px; margin-bottom: 18px; }
  .intro-quote { font-size: 19px; font-weight: 700; margin-top: -6px; }

  .brand { position: absolute; left: 0; top: 380px; width: 950px; height: 150px; }
  .brand-ring {
    position: absolute; left: 152px; top: 0; width: 146px; height: 146px;
    border: 3px solid var(--navy); border-radius: 50%;
  }
  .brand-name {
    position: absolute; left: 318px; top: 28px;
    font-size: 74px; font-weight: 400; color: var(--navy); letter-spacing: -1px; white-space: nowrap;
  }

  .mission {
    position: absolute; left: 31px; top: 548px; width: 888px; height: 100px;
    border: 3px solid var(--navy);
  }
  .mission-title {
    position: absolute; left: 50%; top: -22px; transform: translateX(-50%);
    background: var(--white); padding: 0 14px;
    font-weight: 700; font-size: 28px; color: var(--navy); white-space: nowrap;
  }
  .mission-text {
    padding: 15px 20px 0; text-align: center;
    font-size: 14.3px; line-height: 16.9px; font-weight: 700; color: var(--navy);
  }

  .pillars { position: absolute; left: 0; top: 662px; width: 950px; height: 446px; background: var(--navy); }
  .pillar { position: absolute; top: 32px; width: 262px; }
  .pillar-photo {
    width: 262px; height: 163px; border: 4px solid var(--white);
    box-shadow: 4px 4px 0 rgba(255,255,255,0.35);
  }
  .pillar-text { margin-top: 30px; padding: 0 4px 0 9px; font-size: 13.6px; line-height: 15.1px; }
  .pillar--1 { left: 42px; }
  .pillar--2 { left: 344px; }
  .pillar--3 { left: 645px; }
  .photo-beach { background: linear-gradient(180deg, #c9ced3 0%, #a8aeb2 50%, #c9b9a0 100%); }
  .photo-blossom { background: radial-gradient(circle at 50% 55%, #e89ab5 0%, #b5476e 45%, #3a2a22 100%); }
  .photo-sunset { background: linear-gradient(180deg, #f6c77a 0%, #f08a2c 55%, #b9431a 100%); }

  .contact {
    position: absolute; left: 0; top: 1108px; width: 950px; height: 92px;
    display: flex; align-items: center; justify-content: center;
    font-weight: 900; font-size: 26px; color: var(--navy);
  }
</style>
</head>
<body>
<main class="flyer">
  <svg class="hero-band" viewBox="0 0 950 400" aria-hidden="true">
    <path d="M0 372 C 220 330, 420 355, 620 372 C 760 384, 880 360, 950 330 L950 345 C 880 380, 760 398, 620 392 C 420 382, 220 355, 0 396 Z" fill="var(--swoosh)"/>
    <path d="M0 0 H950 V330 C 880 360, 760 384, 620 372 C 420 355, 220 330, 0 372 Z" fill="var(--navy)"/>
  </svg>

  <div class="portrait" role="img" aria-label="Portrait photo of the coach in a dark blazer and cream knit collar against a brick wall"></div>

  <section class="intro">
    <h1 class="intro-name">Maria Lindqvist Shore</h1>
    <p class="intro-text">I am a modern mystic and leadership developer who has trained several hundreds of leaders on eg. Nordhavn Bank, Mejerigården, Kronbryggeriet, Stegverk, Skyddsam, Vindkraft Nord, Nätbolaget. I have been on my spiritual journey since childhood, meditated since I was 16 and after a decade of extreme skiing and rock climbing I have weighted my adult professional life on the spiritual awakening and to coach people to a more living life.</p>
    <p class="intro-text">With BRIGHT LANTERN I offer opportunities for you as a woman to strengthen contact with your inner being and your own very holy wisdom. To unite the interior with the exterior and deepen your leadership, both as a private person and in your professional role. You are very welcome!</p>
    <p class="intro-quote">"I live as I learn, that's my strength."</p>
  </section>

  <div class="brand">
    <div class="brand-ring"></div>
    <div class="brand-name">Bright Lantern</div>
  </div>

  <section class="mission">
    <h2 class="mission-title">BRIGHT LANTERN</h2>
    <p class="mission-text">We have become good at performing at the expense of contact with our body and soul, when we really need the opposite. A holistic leadership of people who have good self-knowledge, who grow in the challenges, people who know that vulnerability gives an incomparable strength and does not underestimate their brilliant intellect. The world needs people who live and lead from a whole new place. The show feminine can lead us there.</p>
  </section>

  <section class="pillars">
    <article class="pillar pillar--1">
      <div class="pillar-photo photo-beach" role="img" aria-label="Photo of a thoughtful woman in a light shawl on a misty beach"></div>
      <p class="pillar-text">As modern women, many of us share a basic pattern of just pushing through and biting, delivering and being good by driving over both body and soul. What if there is another way to get results? A way in which you combine practical skills in leadership such as goals, performance management and coaching with presence in both body, heart and soul. A way that lets soul, heart, achievement and business go hand in hand.</p>
    </article>
    <article class="pillar pillar--2">
      <div class="pillar-photo photo-blossom" role="img" aria-label="Close-up photo of pink cherry blossoms on a branch"></div>
      <p class="pillar-text">Before spirituality became its own concept and concept, before the word even emerged or religions and new age seized it, it already existed as a natural part of our lives. We are all valuable just by being, without performing. We are all in contact with something bigger, everything is connected and is part of the same being. Life is sacred. Remembering and living this is spirituality for me.</p>
    </article>
    <article class="pillar pillar--3">
      <div class="pillar-photo photo-sunset" role="img" aria-label="Photo of a caped figure standing on a hilltop against an orange sunset"></div>
      <p class="pillar-text">We live in a culture that teaches us to shut down, keep the cover on our dreams and constantly put what is most important to us at the bottom of the list, while we are rushing towards a future that promises us all that we do not take time till now. Bright Lantern is a context that strengthens you, both as being and woman to wake up, grow and succeed with what you want to live before you die. It's empowerment!</p>
    </article>
  </section>

  <footer class="contact">0700-55 01 23 | BRIGHTLANTERN.SE | Folj oss pa: Friendspace</footer>
</main>
</body>
</html>
```